BrightOak Cards, letterhead, and envelopes
BrightOak Technologies and Rx
BrightOak Cards, letterhead, and envelopes - Information Technology
Creative Brief
Use same font as used in my logo
or as you see fit
Professional
Thomas R. Perlavic
President, CEO
4817 S. Harlan Crest Avenue Suite 300
tperlavic@BrightOakTech.example
www.BrightOakTech.example
On the front of the business card please use the BrightOak Technologies logo, the BrightOakTech.example website, and integrate the i graphic with a shadow effect. On the back of the business card, please use the square logo (i with the Rx), the i graphic with the shadow effect and list the BrightOakRx.example website.

```html
<!DOCTYPE html>
<html lang="en">
<head>
<meta charset="utf-8">
<title>BrightOak Technologies – Stationery Set</title>
<link rel="stylesheet" href="https://fonts.googleapis.com/css2?family=Open+Sans:wght@400;600;700&display=swap">
<style>
  :root{
    --bg:#e4e6e9;
    --paper:#ffffff;
    --navy:#0f3563;
    --blue:#1d62a8;
    --sky:#4a90d0;
    --green:#6cb33f;
    --ink:#3c4148;
    --muted:#8a9097;
    --rule:#c9ced4;
    --faint:#eef1f3;
  }
  *{box-sizing:border-box;margin:0;padding:0}
  html,body{width:1200px;height:614px;overflow:hidden}
  body{background:var(--bg);font-family:"Open Sans",sans-serif;color:var(--ink);position:relative}
  .sheet{position:absolute;background:var(--paper);box-shadow:0 2px 8px rgba(0,0,0,.18);overflow:hidden}

  .brand{display:flex;align-items:center;gap:5px;font-family:"Open Sans",sans-serif;font-weight:700;color:var(--navy);line-height:1;white-space:nowrap}
  .brand-dot{border-radius:50%;background:var(--green);flex:none}
  .brand-sub{font-size:5px;letter-spacing:2px;color:var(--muted);text-transform:uppercase;margin-top:2px}

  /* Envelopes */
  .envelope-back{left:30px;top:40px;width:290px;height:125px}
  .envelope-back svg{position:absolute;inset:0}
  .envelope-front{left:30px;top:180px;width:290px;height:125px}
  .envelope-front .brand{position:absolute;left:14px;top:14px;font-size:15px}
  .envelope-front .brand-dot{width:9px;height:9px}
  .envelope-front .return{position:absolute;left:14px;top:40px;font-size:5px;line-height:7px;color:var(--muted)}
  .envelope-front svg{position:absolute;left:0;bottom:0}

  /* Business cards */
  .card-back{left:45px;top:322px;width:210px;height:120px;background:linear-gradient(135deg,var(--sky),var(--blue) 55%,var(--navy));border-radius:6px}
  .card-back .mark{position:absolute;left:50%;top:30px;transform:translateX(-50%);display:flex;flex-direction:column;align-items:center;gap:6px}
  .card-back .mark-square{width:34px;height:34px;border:2px solid #fff;border-radius:6px;background:rgba(255,255,255,.12)}
  .card-back .mark-name{font-weight:700;font-size:11px;color:#fff}
  .card-back .site{position:absolute;left:0;right:0;bottom:12px;text-align:center;font-size:6px;color:#dbe8f5}

  .card-front{left:45px;top:458px;width:210px;height:120px;border-radius:6px}
  .card-front svg{position:absolute;left:0;top:0}
  .card-front .brand{position:absolute;left:32px;top:18px;font-size:11px;gap:4px}
  .card-front .brand-dot{width:7px;height:7px}
  .card-front .person{position:absolute;left:112px;top:20px;font-size:5px;line-height:7px;white-space:nowrap}
  .card-front .person-name{font-weight:700;color:var(--navy);font-size:6px;line-height:8px}
  .card-front .person-title{color:var(--muted);margin-bottom:4px}
  .card-front .site{position:absolute;left:32px;bottom:12px;font-size:5.5px;color:var(--blue)}

  /* Letterhead & fax */
  .letterhead{left:375px;top:38px;width:380px;height:540px}
  .fax-sheet{left:790px;top:38px;width:380px;height:540px}
  .page-brand{position:absolute;left:50%;top:22px;transform:translateX(-50%);font-size:18px}
  .page-brand .brand-dot{width:10px;height:10px}
  .page-brand .brand-sub{text-align:center}
  .fax-sheet .page-brand{transform:none;left:150px}
  .faint-disc{position:absolute;right:-60px;bottom:40px;width:260px;height:260px;border-radius:50%;background:var(--faint)}
  .page-footer{position:absolute;left:0;right:0;bottom:18px;text-align:center;font-size:6px;color:var(--muted);letter-spacing:.3px}

  .fax-title{position:absolute;right:24px;top:30px;font-size:9px;font-weight:700;color:var(--navy);letter-spacing:1px}
  .fax-table{position:absolute;left:22px;top:62px;width:336px;border-collapse:collapse;font-size:6.5px}
  .fax-table td{border:1px solid var(--rule);height:16px;padding:0 5px}
  .fax-table .label{width:48px;background:#f3f5f7;color:var(--navy);font-weight:600}
  .fax-checks{position:absolute;left:22px;top:150px;width:336px;display:flex;justify-content:space-between;font-size:6px;color:var(--ink)}
  .fax-checks span{display:flex;align-items:center;gap:3px}
  .fax-checks span::before{content:"";width:6px;height:6px;border:1px solid var(--muted)}
  .fax-rule{position:absolute;left:22px;right:22px;top:166px;border-top:1px solid var(--rule)}
</style>
</head>
<body>

<div class="sheet envelope-back">
  <svg width="290" height="125" viewBox="0 0 290 125" aria-hidden="true">
    <defs><linearGradient id="flap" x1="0" y1="0" x2="1" y2="1"><stop offset="0" stop-color="#4a90d0"/><stop offset="1" stop-color="#0f3563"/></linearGradient></defs>
    <path d="M0 0 H290 V22 L145 62 L0 22 Z" fill="url(#flap)"/>
    <circle cx="145" cy="40" r="9" fill="#6cb33f"/>
  </svg>
</div>

<div class="sheet envelope-front">
  <div class="brand"><span class="brand-dot"></span><span>BrightOak<div class="brand-sub">Technologies</div></span></div>
  <p class="return">4817 S. Harlan Crest Avenue Suite 300<br>www.BrightOakTech.example</p>
  <svg width="290" height="125" viewBox="0 0 290 125" aria-hidden="true">
    <path d="M0 125 V100 Q120 80 290 118 V125 Z" fill="#1d62a8"/>
    <path d="M0 100 Q120 80 290 118" fill="none" stroke="#6cb33f" stroke-width="2"/>
  </svg>
</div>

<div class="sheet card-back">
  <div class="mark"><span class="mark-square"></span><span class="mark-name">BrightOak</span></div>
  <p class="site">www.BrightOakRx.example</p>
</div>

<div class="sheet card-front">
  <svg width="210" height="120" viewBox="0 0 210 120" aria-hidden="true">
    <defs><linearGradient id="band" x1="0" y1="0" x2="0" y2="1"><stop offset="0" stop-color="#4a90d0"/><stop offset="1" stop-color="#0f3563"/></linearGradient></defs>
    <path d="M0 0 H22 Q12 60 22 120 H0 Z" fill="url(#band)"/>
  </svg>
  <div class="brand"><span class="brand-dot"></span><span>BrightOak</span></div>
  <div class="person">
    <div class="person-name">Thomas R. Perlavic</div>
    <div class="person-title">President, CEO</div>
    <div>Office (555) 014-2270</div>
    <div>Mobile (555) 014-2271</div>
    <div>Fax (555) 014-2272</div>
    <div>tperlavic@BrightOakTech.example</div>
  </div>
  <p class="site">www.BrightOakTech.example</p>
</div>

<div class="sheet letterhead">
  <div class="faint-disc"></div>
  <div class="brand page-brand"><span class="brand-dot"></span><span>BrightOak<div class="brand-sub">Technologies</div></span></div>
  <p class="page-footer">4817 S. Harlan Crest Avenue Suite 300 · T (555) 014-2270 · www.BrightOakTech.example</p>
</div>

<div class="sheet fax-sheet">
  <div class="faint-disc"></div>
  <div class="brand page-brand"><span class="brand-dot"></span><span>BrightOak<div class="brand-sub">Technologies</div></span></div>
  <div class="fax-title">FAX</div>
  <table class="fax-table">
    <tr><td class="label">To</td><td></td><td class="label">From</td><td></td></tr>
    <tr><td class="label">Fax</td><td></td><td class="label">Pages</td><td></td></tr>
    <tr><td class="label">Phone</td><td></td><td class="label">Date</td><td></td></tr>
    <tr><td class="label">Re</td><td></td><td class="label">CC</td><td></td></tr>
  </table>
  <div class="fax-checks">
    <span>Urgent</span><span>For Review</span><span>Please Comment</span><span>Please Reply</span><span>Please Recycle</span>
  </div>
  <div class="fax-rule"></div>
  <p class="page-footer">4817 S. Harlan Crest Avenue Suite 300 · T (555) 014-2270 · www.BrightOakTech.example</p>
</div>

</body>
</html>
```